| 希望する色 | 黄系 |
【 概要 】 PAKUのリッチの制作をお願いします。 ほぼデザインを出来ているのでデータへの落し込みと多少のブラッシュアップをお願い出来ればと思います。 【 依頼内容 】 添付した画像のように1枚の画像に6分割したリッチメニューになります。 ファイル形式:JPG、JPEG、PNG ファイルサイズ:1MB以下 画像サイズ:2500px × 1686px 【 提供素材 】 ・添付ファイルよりご確認下さい。 【 デザインイメージ 】 ・シンプル ・ピクトグラン ・こちらのサイトのPAKUアカウントで使用します https://morizuto.jp/ 良ければ友達追加をしてイメージ頂けますと幸いです。 <a href="https://tsu.ee/Q8pW2RZ"><img src="https://cdn.paku-assets.example/n/paku_add_friends/btn/ja.png" alt="友だち追加" height="36" border="0"></a> ご質問がありましたら、気軽にお問い合わせください。 応募をお待ちしております! |
| 参考記事URL | ||
| https://morizuto.jp/ | ||
どれも素敵なご提案を頂いたのですが一番動線を考えられた作品を選ばせて頂きました。
色々なご提案を頂いたのにお選び出来ずに申し訳ございません。
また色々と今後もお願いをする計画がございますのでぜひ次回もご参画を頂けますと幸いです。

```html
<!DOCTYPE html>
<html lang="ja">
<head>
<meta charset="utf-8">
<title>PAKU メニュー</title>
<link rel="stylesheet" href="https://fonts.googleapis.com/css2?family=M+PLUS+1p:wght@500;700&display=swap">
<style>
  :root {
    --yellow: #ffe600;
    --amber: #fdbb12;
    --ink: #1a1a1a;
    --paper: #ffffff;
  }
  html, body {
    margin: 0;
    padding: 0;
    width: 1200px;
    height: 808px;
    overflow: hidden;
  }
  .menu {
    display: grid;
    grid-template-columns: repeat(3, 400px);
    grid-template-rows: repeat(2, 404px);
    width: 1200px;
    height: 808px;
    font-family: "M PLUS 1p", sans-serif;
    color: var(--ink);
  }
  .tile {
    position: relative;
    display: flex;
    flex-direction: column;
    align-items: center;
  }
  .tile--yellow { background: var(--yellow); }
  .tile--amber { background: var(--amber); }
  .tile__title {
    margin: 38px 0 0;
    padding: 0 4px 4px;
    font-size: 29px;
    font-weight: 500;
    letter-spacing: 0.02em;
    line-height: 1.2;
    white-space: nowrap;
    border-bottom: 2px solid var(--ink);
  }
  .tile__badge {
    position: absolute;
    left: 50%;
    top: 140px;
    width: 216px;
    height: 216px;
    margin-left: -112px;
    border: 4px solid var(--ink);
    border-radius: 50%;
    background: var(--paper);
    display: flex;
    align-items: center;
    justify-content: center;
  }
  .tile__icon { width: 160px; height: 160px; }
  .tile__icon text {
    font-family: "M PLUS 1p", sans-serif;
    font-size: 7px;
    fill: var(--ink);
  }
</style>
</head>
<body>
<main class="menu">
  <section class="tile tile--yellow">
    <h2 class="tile__title">モリズトする</h2>
    <div class="tile__badge">
      <svg class="tile__icon" viewBox="0 0 140 140" role="img" aria-label="ヘッドセットとパソコン">
        <g fill="none" stroke="#1a1a1a" stroke-width="5" stroke-linecap="round">
          <path d="M44 62 V52 a26 26 0 0 1 52 0 V62"/>
          <path d="M96 70 q0 14 -18 16"/>
        </g>
        <rect x="36" y="54" width="14" height="22" rx="5" fill="#1a1a1a"/>
        <rect x="90" y="54" width="14" height="22" rx="5" fill="#1a1a1a"/>
        <rect x="70" y="82" width="10" height="7" rx="3" fill="#1a1a1a"/>
        <rect x="44" y="94" width="52" height="22" rx="3" fill="none" stroke="#1a1a1a" stroke-width="4"/>
        <rect x="16" y="116" width="108" height="8" fill="#1a1a1a"/>
      </svg>
    </div>
  </section>

  <section class="tile tile--amber">
    <h2 class="tile__title">内見予約をする</h2>
    <div class="tile__badge">
      <svg class="tile__icon" viewBox="0 0 140 140" role="img" aria-label="カレンダー">
        <rect x="14" y="22" width="112" height="104" rx="10" fill="#1a1a1a"/>
        <rect x="22" y="46" width="96" height="72" fill="#fff"/>
        <rect x="38" y="10" width="10" height="26" rx="5" fill="#1a1a1a" stroke="#fff" stroke-width="3"/>
        <rect x="92" y="10" width="10" height="26" rx="5" fill="#1a1a1a" stroke="#fff" stroke-width="3"/>
        <g fill="#1a1a1a">
          <rect x="50" y="54" width="14" height="12"/><rect x="70" y="54" width="14" height="12"/><rect x="90" y="54" width="14" height="12"/>
          <rect x="30" y="72" width="14" height="12"/><rect x="50" y="72" width="14" height="12"/><rect x="70" y="72" width="14" height="12"/><rect x="90" y="72" width="14" height="12"/>
          <rect x="30" y="90" width="14" height="12"/><rect x="50" y="90" width="14" height="12"/><rect x="70" y="90" width="14" height="12"/><rect x="90" y="90" width="14" height="12"/>
        </g>
      </svg>
    </div>
  </section>

  <section class="tile tile--yellow">
    <h2 class="tile__title">申し込みをする</h2>
    <div class="tile__badge">
      <svg class="tile__icon" viewBox="0 0 140 140" role="img" aria-label="書類とペン">
        <path d="M24 14 H84 L104 34 V126 H24 Z" fill="#fff" stroke="#1a1a1a" stroke-width="4" stroke-linejoin="round"/>
        <path d="M84 14 V34 H104" fill="none" stroke="#1a1a1a" stroke-width="4" stroke-linejoin="round"/>
        <g stroke="#1a1a1a" stroke-width="4" stroke-linecap="round">
          <line x1="36" y1="48" x2="90" y2="48"/>
          <line x1="36" y1="62" x2="86" y2="62"/>
          <line x1="36" y1="76" x2="80" y2="76"/>
          <line x1="36" y1="90" x2="70" y2="90"/>
          <line x1="36" y1="104" x2="62" y2="104"/>
        </g>
        <g transform="rotate(45 98 84)">
          <rect x="90" y="30" width="16" height="70" fill="#1a1a1a"/>
          <rect x="90" y="30" width="16" height="10" fill="#fff" stroke="#1a1a1a" stroke-width="3"/>
          <path d="M90 100 L98 116 L106 100 Z" fill="#1a1a1a"/>
        </g>
      </svg>
    </div>
  </section>

  <section class="tile tile--amber">
    <h2 class="tile__title">引越し業者の手配をする</h2>
    <div class="tile__badge">
      <svg class="tile__icon" viewBox="0 0 140 140" role="img" aria-label="トラック">
        <rect x="44" y="34" width="88" height="62" fill="#2a2a2a"/>
        <path d="M8 96 V66 L22 48 H42 V96 Z" fill="#1a1a1a"/>
        <path d="M14 66 L24 54 H36 V66 Z" fill="#fff"/>
        <rect x="8" y="94" width="124" height="10" fill="#1a1a1a"/>
        <g fill="#1a1a1a" stroke="#fff" stroke-width="4">
          <circle cx="30" cy="106" r="12"/>
          <circle cx="104" cy="106" r="12"/>
        </g>
        <g fill="#fff"><circle cx="30" cy="106" r="4"/><circle cx="104" cy="106" r="4"/></g>
      </svg>
    </div>
  </section>

  <section class="tile tile--yellow">
    <h2 class="tile__title">ライフラインの手配をする</h2>
    <div class="tile__badge">
      <svg class="tile__icon" viewBox="0 0 140 140" role="img" aria-label="水道・電気・ガス・電話・通信">
        <g fill="#1a1a1a">
          <rect x="16" y="24" width="22" height="8" rx="2"/>
          <rect x="24" y="18" width="6" height="8"/>
          <path d="M30 28 H44 a6 6 0 0 1 6 6 V42 H42 V36 H30 Z"/>
          <path d="M46 47 q-3 5 0 7 q3 -2 0 -7 Z"/>
        </g>
        <text x="32" y="62" text-anchor="middle">水道</text>
        <g fill="none" stroke="#1a1a1a" stroke-width="2.5" stroke-linecap="round">
          <path d="M86 40 a10 10 0 1 1 12 0 V46 H86 Z"/>
          <line x1="88" y1="50" x2="96" y2="50"/>
          <line x1="92" y1="12" x2="92" y2="16"/>
          <line x1="76" y1="20" x2="79" y2="23"/>
          <line x1="108" y1="20" x2="105" y2="23"/>
        </g>
        <text x="110" y="56" text-anchor="middle">電気</text>
        <g fill="#1a1a1a">
          <path d="M58 74 q-5 -8 2 -14 q0 6 4 8 q1 -4 -1 -8 q8 6 2 14 Z"/>
          <path d="M70 74 q-5 -8 2 -14 q0 6 4 8 q1 -4 -1 -8 q8 6 2 14 Z"/>
          <path d="M82 74 q-5 -8 2 -14 q0 6 4 8 q1 -4 -1 -8 q8 6 2 14 Z"/>
          <rect x="52" y="76" width="40" height="4" rx="2"/>
        </g>
        <text x="72" y="90" text-anchor="middle">ガス</text>
        <path d="M24 96 q-4 4 0 12 q6 12 16 16 q6 2 9 -2 l-6 -7 l-5 3 q-6 -4 -8 -10 l4 -4 l-6 -8 Z" fill="#1a1a1a"/>
        <text x="30" y="134" text-anchor="middle">電話</text>
        <g fill="none" stroke="#1a1a1a" stroke-width="2.5">
          <circle cx="106" cy="110" r="14"/>
          <ellipse cx="106" cy="110" rx="6" ry="14"/>
          <line x1="92" y1="110" x2="120" y2="110"/>
          <line x1="94" y1="103" x2="118" y2="103"/>
          <line x1="94" y1="117" x2="118" y2="117"/>
        </g>
        <text x="106" y="134" text-anchor="middle">通信</text>
      </svg>
    </div>
  </section>

  <section class="tile tile--amber">
    <h2 class="tile__title">鍵受渡方法を確認する</h2>
    <div class="tile__badge">
      <svg class="tile__icon" viewBox="0 0 140 140" role="img" aria-label="2本の鍵">
        <g transform="rotate(-40 90 40)">
          <rect x="58" y="32" width="24" height="16" rx="3" fill="#fff" stroke="#1a1a1a" stroke-width="4"/>
          <path d="M82 22 H112 a6 6 0 0 1 6 6 V52 a6 6 0 0 1 -6 6 H82 Z" fill="#fff" stroke="#1a1a1a" stroke-width="4"/>
          <rect x="100" y="32" width="8" height="16" rx="3" fill="#1a1a1a"/>
          <path d="M58 34 H16 V46 H24 V54 H32 V46 H38 V54 H46 V46 H58 Z" fill="#fff" stroke="#1a1a1a" stroke-width="4" stroke-linejoin="round"/>
        </g>
        <g transform="rotate(-40 100 96)">
          <circle cx="112" cy="96" r="18" fill="#fff" stroke="#1a1a1a" stroke-width="4"/>
          <circle cx="112" cy="96" r="6" fill="#1a1a1a"/>
          <path d="M94 90 H30 V102 H40 V112 H50 V102 H58 V110 H68 V102 H94 Z" fill="#fff" stroke="#1a1a1a" stroke-width="4" stroke-linejoin="round"/>
        </g>
      </svg>
    </div>
  </section>
</main>
</body>
</html>
```